Business card and stationary for NMV Counseling
NMV Counseling - Bramblewood Support Circle, LLC
Business card and stationary for NMV Counseling - Health
Creative Brief
Bright & Fun-filled
Daniel H. Ostrander
MS, MBA, RMHCI
NMV Counseling Bramblewood Support Circle, LLC 4870 W Hazelmere Avenue Orlando, FL 32806
nmvcounseling@mailvista.example
www.nmvcounseling.example
KPT58371
Tie colors into website: www.nmvcounseling.example I'd like to see options for a one side and two sided card.
Text for back of card to include: Next Appointment For: Date: Time: If you are unable to keep appointment, please provide at least 24 hours notice to avoid a fee. === Individual Couples Men's Issues Business Professionals Career Counseling

```html
<!DOCTYPE html>
<html lang="en">
<head>
<meta charset="utf-8">
<title>Quillmont Counseling – Appointment Card</title>
<link rel="stylesheet" href="https://fonts.googleapis.com/css2?family=Questrial&display=swap">
<style>
  :root {
    --backdrop: #d9d9db;
    --card: #ffffff;
    --indigo: #34307f;
    --sky: #8fc3ea;
    --ink: #2b2b33;
    --rule: #6b6b78;
    --box: #3a3a44;
  }
  * { margin: 0; padding: 0; box-sizing: border-box; }
  html, body {
    width: 1200px; height: 901px; overflow: hidden;
    background: var(--backdrop);
    font-family: "Questrial", "Century Gothic", sans-serif;
    color: var(--ink);
  }
  .appointment-card {
    position: absolute; left: 110px; top: 170px;
    width: 980px; height: 560px;
    background: var(--card);
    box-shadow: 0 12px 40px rgba(0,0,0,.18);
    padding: 50px 56px;
  }
  .card-title {
    font-size: 40px; font-weight: 400; color: var(--indigo);
    letter-spacing: .5px; line-height: 1.2;
  }
  .brand {
    position: absolute; right: 56px; top: 56px;
    display: flex; align-items: center; gap: 12px;
  }
  .brand-dot { width: 30px; height: 30px; border-radius: 50%; background: var(--sky); flex: none; }
  .brand-name { font-size: 24px; color: var(--indigo); white-space: nowrap; }
  .field-row {
    display: flex; align-items: baseline; gap: 60px;
    font-size: 27px; margin-top: 36px; line-height: 1.2;
  }
  .field { display: flex; align-items: baseline; gap: 10px; white-space: nowrap; }
  .field-line {
    display: inline-block; border-bottom: 2px dotted var(--rule);
    height: 1px; transform: translateY(-6px);
  }
  .field-line.name { width: 260px; }
  .field-line.date { width: 150px; }
  .field-line.time { width: 170px; }
  .weekdays {
    display: flex; justify-content: space-between;
    margin-top: 48px; font-size: 25px;
  }
  .day { display: flex; align-items: center; gap: 8px; }
  .day-box { width: 24px; height: 24px; border: 2px solid var(--box); border-radius: 4px; }
  .notice { margin-top: 40px; font-size: 17px; line-height: 1.3; }
  .services {
    position: absolute; left: 56px; right: 56px; bottom: 60px;
    display: flex; justify-content: space-between; font-size: 19px;
    list-style: none;
  }
</style>
</head>
<body>
  <section class="appointment-card">
    <h1 class="card-title">Your Appointment</h1>
    <div class="brand">
      <span class="brand-dot"></span>
      <span class="brand-name">Quillmont Counseling</span>
    </div>

    <div class="field-row">
      <div class="field">Name : <span class="field-line name"></span></div>
    </div>
    <div class="field-row">
      <div class="field">Date : <span class="field-line date"></span></div>
      <div class="field">Time : <span class="field-line time"></span> am/pm</div>
    </div>

    <div class="weekdays">
      <div class="day"><span class="day-box"></span>Mon</div>
      <div class="day"><span class="day-box"></span>Tue</div>
      <div class="day"><span class="day-box"></span>Wed</div>
      <div class="day"><span class="day-box"></span>Thu</div>
      <div class="day"><span class="day-box"></span>Fri</div>
      <div class="day"><span class="day-box"></span>Sat</div>
    </div>

    <p class="notice">If you are unable to keep appointment, please provide at least 24 hour notice to avoid a fee.</p>

    <ul class="services">
      <li>Individual</li>
      <li>Couples</li>
      <li>Men's Issues</li>
      <li>Business Professionals</li>
      <li>Career Counseling</li>
    </ul>
  </section>
</body>
</html>
```